International house cleaning business needs Marketing Landing Page for improving user acquisition

We are in need of an additional marketing Landing Page that we can use to test and improve our user acquisition. We will be looking at a minimum of one page selection, but are open to awarding up to 5 depending on the quality of work and the different variables to test.

Our current homepages are www.tidlyo.com and https://www.tidlyo.com/lps/firstnhours.aspx?c=MARKETING39&city=Toronto&gclid=CIqXg7z_wsECFUKCMgodknwAGA and we are looking for ways that will improve 1) Account Creation and 2) Appointment Bookings by making them more simple. Please look at the entire process and address the main issues in the Landing Page that you create.

Competitors include www.scrubvix.com and www.pravelo.com

The design will be entirely up to your discretion, however the required aspects are below:

1) Maintain Corporate color scheme
2) Target audience are new users coming from offer based marketing campaigns
3) Will need an area of the page with a changeable 'offer message'
4) The offer area mentioned above should also be easily removable if there is no offer
5) The focus is on new users but we will still need to have a visible 'sign in button' for returning users
6) Linkumo login and create account with email CTA's both must be large and visible
7) Opt-in for eNewsletter button when email address is collected
8) We also have a short informative video so feel free to incorporate that in a version

General Ideas:

*email collection on Landing Page to start engagement early
*email and postal code collection on Landing Page to start engagement early
*general information and booking form on the HP to reduce the click needed to get to account creation or booking
*"Tell Us About Your Place" info (# of beds and # of baths) on HP to get process started (similar to www.nestqor.com)

Good Examples:

www.linkumo.com (merges info and sign-up)
www.nestqor.com (early engagement)
www.raxo.com (early engagement)

```html
<!DOCTYPE html>
<html lang="en">
<head>
<meta charset="utf-8">
<title>Tidlyo – Book a Trusted Cleaning Professional</title>
<link rel="stylesheet" href="https://fonts.googleapis.com/css2?family=Figtree:wght@300;400;500;600;700&display=swap">
<style>
  :root {
    --page-top: #d9d9d9;
    --page-bottom: #eeeeee;
    --brand-coral: #ec6a5e;
    --brand-coral-dark: #d9544a;
    --social-blue: #3b5ba5;
    --social-blue-dark: #2c4687;
    --ink: #0d0d0d;
    --body-grey: #6a6a6a;
    --link-blue: #2a9fd8;
    --kraft: #d5b27c;
    --kraft-light: #ddbe8c;
    --teal: #3bc4a8;
    --white: #ffffff;
    --placeholder: #8a8a8a;
  }
  * { box-sizing: border-box; margin: 0; padding: 0; }
  html, body { width: 1200px; height: 996px; overflow: hidden; }
  body {
    position: relative;
    font-family: "Figtree", Arial, sans-serif;
    background: linear-gradient(to bottom, var(--page-top) 0 548px, var(--page-bottom) 548px);
  }

  .account-bar { position: absolute; top: 28px; right: 89px; display: flex; gap: 8px; }
  .account-btn {
    height: 31px; border-radius: 3px; color: var(--white);
    font-size: 10.5px; font-weight: 600; display: flex; align-items: center;
    justify-content: center; text-decoration: none;
  }
  .account-btn--email { width: 147px; background: var(--brand-coral); border: 1px solid var(--brand-coral-dark); }
  .account-btn--social { width: 147px; background: var(--social-blue); border: 1px solid var(--social-blue-dark); justify-content: flex-start; }
  .account-btn__square { width: 28px; height: 29px; background: var(--social-blue-dark); margin-right: 12px; }

  .page { position: absolute; left: 99px; top: 82px; width: 1012px; }

  .hero { position: relative; height: 519px; overflow: hidden;
    background: linear-gradient(100deg, #e4e4e0 0%, #f4f4f2 35%, #e9e9e6 60%, #f3f3f1 100%); }
  .hero__helper {
    position: absolute; right: 0; top: 0; width: 272px; height: 519px;
    background: linear-gradient(180deg, #f2f2f0 0%, #f7f7f5 30%, #8fcfc4 65%, #3fb5ad 100%);
  }
  .brand { position: absolute; left: 68px; top: 40px; color: var(--brand-coral);
    font-size: 34px; font-weight: 600; letter-spacing: -0.5px; }
  .hero__title { position: absolute; left: 68px; top: 134px; width: 500px;
    font-size: 51px; font-weight: 600; line-height: 66px; color: var(--ink); letter-spacing: -1px; }
  .hero__lead { position: absolute; left: 68px; top: 342px; width: 500px;
    font-size: 20px; font-weight: 400; line-height: 27px; color: #1a1a1a; }

  .quote-form { position: absolute; left: 593px; top: 144px; width: 351px; height: 375px;
    background: radial-gradient(circle at 30% 30%, var(--kraft-light), var(--kraft) 70%); padding: 0 29px; }
  .quote-form__title { text-align: center; font-size: 25px; font-weight: 600; color: var(--ink); margin-top: 27px; letter-spacing: -0.4px; }
  .quote-form__grid { display: grid; grid-template-columns: 138px 138px; column-gap: 16px; row-gap: 15px; margin-top: 27px; }
  .field { height: 31px; background: var(--white); font-family: inherit; font-size: 12px; font-weight: 500;
    color: var(--placeholder); padding: 0 7px; display: flex; align-items: center; }
  .field--filled { background: transparent; border: 1px solid rgba(255,255,255,.8); color: var(--ink); font-weight: 600; }
  .field--message { height: 71px; margin-top: 16px; background: transparent; border: 1px solid rgba(255,255,255,.8); position: relative; }
  .field--message svg { position: absolute; right: 6px; bottom: 6px; }
  .quote-form__submit { margin-top: 15px; width: 160px; height: 35px; background: var(--teal); color: var(--white);
    font-size: 23px; font-weight: 700; display: flex; align-items: center; justify-content: center; }

  .intro { height: 270px; background: var(--white); text-align: center; padding-top: 56px; }
  .intro__title { font-size: 25px; font-weight: 600; color: var(--ink); letter-spacing: -0.4px; }
  .intro__text { width: 870px; margin: 16px auto 0; font-size: 16.5px; font-weight: 400; line-height: 27px; color: var(--body-grey); }
  .intro__text a { color: var(--link-blue); text-decoration: none; }

  .services { height: 125px; background: var(--teal); position: relative; }
  .services__tile { position: absolute; top: 61px; width: 203px; height: 64px; }
  .services__tile:nth-child(1) { left: 67px; background: linear-gradient(#e9c3ac, #d9a98e); }
  .services__tile:nth-child(2) { left: 292px; background: linear-gradient(#6b5a4e, #a38f7f); }
  .services__tile:nth-child(3) { left: 517px; background: linear-gradient(#b4a391, #d8cbb8); }
  .services__tile:nth-child(4) { left: 742px; background: linear-gradient(#cdbfb4, #eae6e2); }
</style>
</head>
<body>
  <nav class="account-bar">
    <a class="account-btn account-btn--email" href="#">Login with Tidlyo.com</a>
    <a class="account-btn account-btn--social" href="#"><span class="account-btn__square"></span>Login with Linkumo</a>
  </nav>

  <main class="page">
    <section class="hero" role="img" aria-label="Bright living room with white sofa and large windows">
      <div class="hero__helper" role="img" aria-label="Smiling cleaning professional in uniform holding cleaning supplies"></div>
      <div class="brand">Tidlyo</div>
      <h1 class="hero__title">Book a Trusted Cleaning Professional Today.</h1>
      <p class="hero__lead">Get your home in order with courteous professional cleaners. Just schedule when and we'll be at your door in no time.</p>

      <form class="quote-form">
        <h2 class="quote-form__title">Ask for quote now.</h2>
        <div class="quote-form__grid">
          <div class="field field--filled">Joris Kamphuis</div>
          <div class="field">address</div>
          <div class="field">postalcode</div>
          <div class="field">place</div>
          <div class="field">phone number</div>
          <div class="field">email@adres.nl</div>
        </div>
        <div class="field field--message">
          <svg width="8" height="8" viewBox="0 0 8 8"><g fill="#fff"><rect x="6" y="0" width="2" height="2"/><rect x="3" y="3" width="2" height="2"/><rect x="6" y="3" width="2" height="2"/><rect x="0" y="6" width="2" height="2"/><rect x="3" y="6" width="2" height="2"/><rect x="6" y="6" width="2" height="2"/></g></svg>
        </div>
        <div class="quote-form__submit">send quote</div>
      </form>
    </section>

    <section class="intro">
      <h2 class="intro__title">Book a Cleaning Today.</h2>
      <p class="intro__text">Wij bieden u een uitgebreid scala aan activiteiten. Naast algehele <a href="#">stucadoorswerkzaamheden</a> is onze specialiteit Wandstyling: een exclusieve wanddecoratievorm die een speciale techniek vereist. Met behulp van kleurrijke sierpleisters in combinatie met <a href="#">stijlvolle</a> Italiaanse stucco-materialen worden fantastische wandafwerkingen gecreëerd.</p>
    </section>

    <section class="services">
      <div class="services__tile" role="img" aria-label="Worker plastering a wall"></div>
      <div class="services__tile" role="img" aria-label="Craftsman smoothing a surface"></div>
      <div class="services__tile" role="img" aria-label="Worker finishing a stucco hallway"></div>
      <div class="services__tile" role="img" aria-label="Craftsman restoring a decorative ceiling"></div>
    </section>
  </main>
</body>
</html>
```